Yoga Shool offering Teacher Training in a new venue

I need to advertise our 200Hr Teacher Training course at the Fernhill Arena, I want to attract yoga students who want to be teachers as well as those looking to deepen their personal practice and attend for personal growth. I introduced yoga classes to this venue when it first opened in 2000, and I am returning with this Teacher Training course. My website colours are brown and orange.

Target Market(s)

Yoga Students around the venue

Font styles to use
Sans Serif

Colors

Designer to choose colors to be used in the design.

Requirements
Must have
• logo,

```html
<!DOCTYPE html>
<html lang="en">
<head>
<meta charset="utf-8">
<title>Yoga Cadence Teacher Training – Fernhill Arena</title>
<link rel="stylesheet" href="https://fonts.googleapis.com/css2?family=Montserrat:wght@700;800&family=Open+Sans:wght@400;800&family=Didact+Gothic&display=swap">
<style>
  :root {
    --orange: #ee7a0a;
    --orange-dark: #c9630a;
    --brown: #5e3c37;
    --paper: #f3eeec;
    --ink: #2e2322;
    --white: #ffffff;
    --page-bg: #8a8a8a;
  }
  * { margin: 0; padding: 0; box-sizing: border-box; }
  html, body { width: 1200px; height: 1200px; overflow: hidden; background: var(--page-bg); }
  .flyer {
    position: absolute; left: 193px; top: 25px; width: 814px; height: 1150px;
    background: var(--paper); overflow: hidden;
    font-family: "Didact Gothic", "Century Gothic", sans-serif; color: var(--ink);
  }
  .hero-photo {
    position: absolute; left: 0; top: 0; width: 814px; height: 622px;
    background: linear-gradient(180deg, #7f8f6a 0%, #5c7448 45%, #76914f 70%, #5b6f8e 88%, #4f638a 100%);
  }
  .hero-shapes { position: absolute; left: 0; top: 0; }
  .brand-mark {
    position: absolute; left: 39px; top: 32px; width: 138px; height: 138px; border-radius: 50%;
    background: var(--brown); display: flex; align-items: center; justify-content: center; text-align: center;
    color: var(--orange); font-family: "Open Sans", sans-serif; font-weight: 800; font-size: 22px; line-height: 1.1;
  }
  .hero-title {
    position: absolute; left: 39px; top: 190px; color: var(--white);
    font-family: "Open Sans", sans-serif; font-weight: 800; font-size: 33px; letter-spacing: .5px;
  }
  .hero-sub {
    position: absolute; left: 39px; top: 238px; width: 270px; color: var(--white);
    font-family: "Open Sans", sans-serif; font-size: 26px; line-height: 29px;
  }
  .course-title {
    position: absolute; left: 39px; top: 633px; width: 720px; color: var(--brown);
    font-family: "Montserrat", sans-serif; font-weight: 800; font-size: 22px; line-height: 34px; letter-spacing: .3px;
  }
  .course-question {
    position: absolute; left: 37px; top: 701px; color: var(--orange);
    font-family: "Montserrat", sans-serif; font-weight: 700; font-size: 14.5px;
  }
  .for-you-tag {
    position: absolute; left: 0; top: 732px; width: 205px; height: 28px; background: var(--brown);
    color: var(--white); font-size: 18px; line-height: 28px; padding-left: 38px;
  }
  .intro {
    position: absolute; left: 38px; top: 771px; width: 463px; font-size: 13.5px; line-height: 21px; text-align: justify;
  }
  .next-step {
    position: absolute; left: 38px; top: 840px; width: 463px; color: var(--orange);
    font-size: 16.5px; line-height: 20px; text-align: justify;
  }
  .testimonial {
    position: absolute; top: 894px; width: 141px; font-size: 11px; line-height: 14.7px; text-align: justify;
  }
  .t1 { left: 38px; } .t2 { left: 194px; } .t3 { left: 350px; }
  .side-photo {
    position: absolute; left: 517px; top: 775px; width: 266px; height: 265px;
    background: linear-gradient(180deg, #4e6b3b 0%, #6f8e4f 45%, #7fae55 70%, #5a4a42 100%);
  }
  .contact-band { position: absolute; left: 0; top: 1055px; width: 814px; height: 95px; background: var(--brown); }
  .web-tab { position: absolute; left: 0; top: 1010px; }
  .web-line {
    position: absolute; left: 48px; width: 290px; text-align: center; color: var(--white);
    font-family: "Open Sans", sans-serif; font-size: 16px;
  }
  .web-line b { font-weight: 800; }
  .web-url { top: 1051px; } .web-mail { top: 1117px; }
  .tab-icon { position: absolute; left: 180px; }
  .phone-icon { position: absolute; left: 328px; top: 1082px; }
  .phone-number {
    position: absolute; left: 371px; top: 1074px; color: var(--white);
    font-family: "Montserrat", sans-serif; font-weight: 800; font-size: 36px; letter-spacing: .5px;
  }
  .divider { position: absolute; left: 654px; top: 1068px; width: 1.5px; height: 56px; background: var(--white); }
  .follow-label { position: absolute; left: 682px; top: 1068px; color: var(--white); font-size: 17px; }
  .social-dots { position: absolute; left: 672px; top: 1102px; display: flex; gap: 11px; }
  .social-dots span { width: 18px; height: 18px; border-radius: 50%; background: var(--white); display: block; }
</style>
</head>
<body>
<main class="flyer">
  <div class="hero-photo" role="img" aria-label="Photo of a yoga teacher holding warrior two pose on a blue mat on grass in front of tall reeds"></div>
  <svg class="hero-shapes" width="814" height="622" viewBox="0 0 814 622" aria-hidden="true">
    <polygon points="460,192 472,185 12,622 0,622" fill="var(--brown)"/>
    <polygon points="0,0 294,0 471,185 0,620" fill="var(--orange)"/>
  </svg>
  <div class="brand-mark">Yoga<br>Cadence</div>
  <h1 class="hero-title">ARE YOU READY?</h1>
  <p class="hero-sub">to set in motion a stunning transformation in 2019</p>

  <h2 class="course-title">YOGA CADENCE TEACHER TRAINING IS COMING TO<br>THE FERNHILL ARENA</h2>
  <p class="course-question">Do you want to know yourself, love yourself, heal yourself and treat yourself better?</p>
  <div class="for-you-tag">THIS IS FOR YOU!</div>
  <p class="intro">Yoga Cadence Teacher Training isn’t just for aspiring teachers, it’s for any dedicated student of yoga to build a powerful personal practice and deepen their understanding and experience of yoga.</p>
  <p class="next-step">Take the next step in your yoga and in your life, access new possibilities, check out what past trainees had to say:</p>
  <p class="testimonial t1">“Wow! This course has been life changing in every way, it has given me so much confidence to do things I haven’t done before.” Dana Ellery 2018</p>
  <p class="testimonial t2">“I love how we apply everything to our own lives – it’s real and tangible, so we live it and learn it…” Milo Grant Hughes 2016</p>
  <p class="testimonial t3">“I loved every lesson, and as I applied the teachings to my life, they had a flow on effect to my family too. Prepare to not only become a yoga teacher, prepare to change in incredibly positive ways.” Tessa Royle 2018</p>
  <div class="side-photo" role="img" aria-label="Photo of the teacher seated in a wide squat on a wooden stool in a garden"></div>

  <div class="contact-band"></div>
  <svg class="web-tab" width="340" height="140" viewBox="0 0 340 140" aria-hidden="true">
    <polygon points="26,45 44,0 44,45" fill="var(--orange-dark)"/>
    <polygon points="318,45 300,0 300,45" fill="var(--orange-dark)"/>
    <polygon points="44,0 300,0 318,45 300,140 60,140 26,45" fill="var(--orange)"/>
  </svg>
  <svg class="tab-icon" style="top:1019px" width="26" height="26" viewBox="0 0 26 26" aria-hidden="true">
    <g fill="none" stroke="var(--white)" stroke-width="2"><circle cx="13" cy="13" r="11"/><ellipse cx="13" cy="13" rx="5" ry="11"/><line x1="2" y1="13" x2="24" y2="13"/><line x1="4" y1="7" x2="22" y2="7"/><line x1="4" y1="19" x2="22" y2="19"/></g>
  </svg>
  <p class="web-line web-url">www.<b>yogacadence</b>.com.au</p>
  <svg class="tab-icon" style="top:1085px" width="26" height="26" viewBox="0 0 26 26" aria-hidden="true">
    <g fill="none" stroke="var(--white)" stroke-width="2"><circle cx="13" cy="13" r="11"/><rect x="7" y="9" width="12" height="8"/><polyline points="7,9 13,14 19,9"/></g>
  </svg>
  <p class="web-line web-mail">hello@<b>yogacadence</b>.com.au</p>

  <svg class="phone-icon" width="32" height="32" viewBox="0 0 32 32" aria-hidden="true">
    <g fill="none" stroke="var(--white)" stroke-width="2.2"><circle cx="16" cy="16" r="14"/><path d="M10 9c-1 4 4 12 9 14l3-3-3-3-2 1c-2-1-4-3-5-5l1-2-3-3z"/></g>
  </svg>
  <p class="phone-number">61455018264</p>
  <div class="divider"></div>
  <p class="follow-label">Follow Us:</p>
  <div class="social-dots" aria-label="Social media links"><span></span><span></span><span></span><span></span></div>
</main>
</body>
</html>
```